website for Facial Plastic Surgeon

We are in need of a modern, captivating and aesthetically pleasing website for MK Facial Plastics.
The website must be informative whilst flowing with ease and also entice patients to explore their options with the procedures we have available.
It is essential that the website is compatible across all devices and user friendly, especially when it comes to updating details within the website etc.
The pages we would require are:
Home, About, Procedures, Gallery & Contact
Procedures included on our website should be as follows:
Anti wrinkle injections and fillers
Necklifts
Brow lift
Facial scar revision
Rhytidectomy or Face lift
Chin implants
Rhinoplasty
Otoplasty or Pinnaplasty
Blepharoplasty or Upper and Lower Eyelid Surgery
Given the multiple locations of which we currently consult and operate from, our contact page should include a clear map outlining each clinic location.
- 48 Tolland Street Echuca VIC 3550
- 312 Mirren Street Bendigo Vic 3550
- Level 3, 415 Hadley Street, Epping Vic 3076
- Level 6, 187 Brenton Street Melbourne Vic 3000
Our new logo and examples of our stationary are also attached for your reference.
The following links below are examples of other websites that we like:
Example #1 https://www.brightvalefaceclinic.example/
Example #2 https://www.meridowsurgicalcare.example/
Example #3 https://www.larkstonecosmeticcentre.example/
There is opportunity for further work within another branch of our business for the successful candidate
Target Market(s)
Adults of all ages
Coding
Coded - Design and coding required
Number of Pages Required
5+ page
Requirements
Must have
- Modern
- Captivating
- Aesthetically pleasing

```html
<!DOCTYPE html>
<html lang="en">
<head>
<meta charset="utf-8">
<title>MK Facial Plastics</title>
<link rel="stylesheet" href="https://fonts.googleapis.com/css2?family=Great+Vibes&family=Lora:wght@400;700&display=swap">
<style>
:root{
  --ink:#2b2b2b;
  --muted:#555;
  --gold:#b49f7b;
  --sand:#c8bb9f;
  --ring:#c9bd9f;
  --services:#c3b091;
  --newsletter:#cbc0a6;
  --gallery-bg:#ececec;
  --footer:#1f1f1f;
  --white:#fff;
}
*{box-sizing:border-box;margin:0;padding:0}
html,body{width:1200px;height:5240px;overflow:hidden}
body{position:relative;font-family:"Lora",Georgia,serif;color:var(--ink);background:var(--white)}
.abs{position:absolute}
.script{font-family:"Great Vibes",cursive;font-weight:400;color:var(--ink)}
.section-title{position:absolute;left:0;width:1200px;text-align:center;font-size:58px;line-height:1}
.btn{position:absolute;display:flex;align-items:center;justify-content:center;border:1.5px solid var(--ink);font-size:15px;font-weight:700;color:var(--ink);background:transparent}
.photo{position:absolute;border-radius:50%}

/* hero */
.hero{position:absolute;left:0;top:0;width:1200px;height:740px;background:linear-gradient(100deg,#f4f1ee 0%,#ece7e2 40%,#d9d4d0 70%,#e8e5e2 100%)}
.hero-mirror{left:680px;top:80px;width:480px;height:520px;border-radius:50%;background:radial-gradient(circle at 50% 45%,#f1d9c8 0%,#e8cdb9 45%,#f3f3f3 72%,#e3e3e3 100%)}
.brand{left:92px;top:62px;display:flex;align-items:center;gap:12px;font-size:17px;color:var(--ink)}
.brand-dot{width:14px;height:14px;border-radius:50%;background:var(--gold)}
.topbar{right:92px;top:20px;display:flex;gap:44px;font-size:15px}
.topbar span{display:flex;align-items:center;gap:10px}
.nav{right:92px;top:74px;display:flex;gap:44px;font-size:15px;letter-spacing:.3px}
.nav .active{color:var(--gold)}
.hero-title{left:92px;top:268px;font-size:50px;font-weight:400;line-height:60px;color:var(--ink)}
.hero-sub{left:118px;top:358px;width:560px;font-size:23px;line-height:31px;color:var(--ink)}
.hero-arrows{left:88px;top:618px}

/* about */
.about-ring{left:84px;top:820px;width:504px;height:504px;border-radius:50%;background:var(--ring)}
.about-photo{left:106px;top:842px;width:460px;height:460px;background:linear-gradient(135deg,#e9e3e0,#d7b8a5 45%,#b7c2d6 80%,#e7e7ee)}
.about-title{left:616px;top:880px;font-size:60px}
.about-text{left:616px;top:962px;width:470px;font-size:15.5px;line-height:30.5px;color:var(--muted)}

/* services */
.services{position:absolute;left:0;top:1399px;width:1200px;height:1056px;background:radial-gradient(ellipse at 50% 35%,#d6c7b0 0%,#c7b598 40%,var(--services) 100%)}
.svc{position:absolute;width:280px;text-align:center;font-size:17px;font-weight:700;line-height:26px}
.svc-ring{position:absolute;width:272px;height:272px;border:1.5px solid #3b3226;border-radius:50%}
.svc-photo{position:absolute;width:230px;height:230px;border-radius:50%;border:2px solid #3b3226}

/* why */
.why{position:absolute;left:0;top:2455px;width:1200px;height:476px;background:linear-gradient(120deg,#8c8a87 0%,#7d7a76 40%,#86807a 70%,#948d86 100%)}
.stat{position:absolute;width:200px;height:200px;border:1.5px solid rgba(255,255,255,.8);border-radius:50%;color:var(--white);text-align:center}
.stat .num{margin-top:40px;font-size:38px;font-weight:400;line-height:44px}
.stat .num small{font-size:16px}
.stat .cap{margin-top:8px;font-size:19px;line-height:23px}

/* testimonials */
.card{position:absolute;top:3139px;width:324px;height:250px;background:var(--white);border-radius:6px;box-shadow:0 2px 10px rgba(0,0,0,.12)}
.quote{position:absolute;left:37px;top:-24px;width:50px;height:50px;background:var(--sand);display:flex;align-items:center;justify-content:center}
.card h3{position:absolute;left:34px;top:54px;font-size:20px;font-weight:400}
.card p{position:absolute;left:34px;top:100px;width:270px;font-size:14px;line-height:28px;color:var(--muted)}
.card a{position:absolute;left:34px;top:204px;font-size:14px;font-weight:700;color:var(--ink);text-decoration:underline}

/* gallery */
.gallery{position:absolute;left:0;top:3486px;width:1200px;height:505px;background:var(--gallery-bg)}
.gphoto{position:absolute;top:179px;width:192px;height:192px;border-radius:50%;border:3px solid var(--white)}
.dots{position:absolute;left:578px;top:400px;display:flex;gap:10px}
.dots i{width:7px;height:7px;border-radius:50%;background:#777}
.dots i:first-child{background:#bbb}

/* newsletter */
.newsletter{position:absolute;left:0;top:3991px;width:1200px;height:177px;background:var(--newsletter)}
.nl-title{left:92px;top:58px;font-size:52px;line-height:1;white-space:nowrap}
.nl-field{position:absolute;left:596px;top:65px;width:515px;height:53px;background:var(--white);border-radius:27px;display:flex;align-items:center;justify-content:space-between;padding:0 28px;font-size:15px;color:#999}

/* locations */
.map{position:absolute;top:4353px;width:236px;height:236px;border-radius:50%;border:1px solid #ddd;background:linear-gradient(135deg,#f3f1ec,#e6e4df 50%,#efeee9)}
.loc{position:absolute;top:4603px;width:260px;text-align:center;font-size:16px;line-height:25px}

/* footer */
.footer{position:absolute;left:0;top:4740px;width:1200px;height:500px}
.fcol{position:absolute;top:160px;color:var(--white)}
.fcol h4{font-size:17px;font-weight:700;letter-spacing:.3px;margin-bottom:18px}
.fcol li{list-style:none;font-size:13px;line-height:31px}
.socials{display:flex;gap:22px;margin-top:4px}
.socials i{width:14px;height:14px;border-radius:50%;background:var(--white)}
.copy{position:absolute;left:0;top:452px;width:1200px;text-align:center;color:var(--white);font-size:11px}
</style>
</head>
<body>

<!-- HERO -->
<header class="hero">
  <div class="abs hero-mirror" role="img" aria-label="Photo of a woman touching her face, reflected in a round mirror"></div>
  <div class="abs brand"><span class="brand-dot"></span><span>MK Facial Plastics</span></div>
  <div class="abs topbar">
    <span><svg width="15" height="12" viewBox="0 0 15 12"><rect x="0.5" y="0.5" width="14" height="11" fill="#2b2b2b"/><path d="M1 1l6.5 5L14 1" stroke="#fff" fill="none"/></svg>info@mkfacialplastics.example</span>
    <span><svg width="14" height="14" viewBox="0 0 24 24"><path fill="#2b2b2b" d="M6.6 10.8a15 15 0 006.6 6.6l2.2-2.2c.3-.3.7-.4 1-.2 1.1.4 2.3.6 3.6.6.6 0 1 .4 1 1V20c0 .6-.4 1-1 1A17 17 0 013 4c0-.6.4-1 1-1h3.5c.6 0 1 .4 1 1 0 1.3.2 2.5.6 3.6.1.3 0 .7-.2 1z"/></svg>03 5550 1187</span>
  </div>
  <nav class="abs nav">
    <span class="active">HOME</span><span>ABOUT</span><span>PROCEDURES</span><span>GALLERY</span><span>CONTACT</span>
  </nav>
  <h1 class="abs hero-title">MK Facial Plastics</h1>
  <p class="abs hero-sub">Lorem ipsum dolor sit amet, consectetur adipiscing elit, sed do eiusmod tempor</p>
  <div class="btn" style="left:118px;top:445px;width:180px;height:47px;font-weight:400">Get Free Consulting</div>
  <svg class="abs hero-arrows" width="80" height="30" viewBox="0 0 80 30"><path d="M14 4L4 15l10 11M56 4l10 11-10 11" stroke="#2b2b2b" stroke-width="2" fill="none"/></svg>
</header>
<svg class="abs" style="left:0;top:640px" width="1200" height="110" viewBox="0 0 1200 110">
  <path d="M0 45 C150 70 300 95 430 60 L435 52 L440 60 C560 95 760 70 900 45 C1000 30 1120 15 1200 10 L1200 110 L0 110Z" fill="#fff"/>
  <path d="M0 45 C150 70 300 95 430 60 L435 52 L440 60 C560 95 760 70 900 45 C1000 30 1120 15 1200 10" stroke="#c9bd9f" stroke-width="5" fill="none"/>
</svg>

<!-- ABOUT -->
<section>
  <div class="abs about-ring"></div>
  <div class="photo about-photo" role="img" aria-label="Photo of a woman receiving a facial skin treatment"></div>
  <h2 class="abs script about-title">About Us</h2>
  <p class="abs about-text">Lorem ipsum dolor sit amet, consectetur adipiscing elit, sed do eiusmod tempor incididunt ut labore et dolore magna aliqua. Ut enim ad minim veniam, quis nostrud exercitation ullamco laboris nisi ut aliquip ex ea commodo consequat. Duis aute irure dolor in reprehenderit in voluptate velit esse cillum dolore eu fugiat nulla pariatur. Excepteur sint occaecat cupidatat non proident, sunt in culpa qui officia deserunt mollit anim id est laborum</p>
  <div class="btn" style="left:616px;top:1202px;width:151px;height:51px;border-color:#999">Read More</div>
</section>

<!-- SERVICES -->
<section class="services" role="img" aria-label="Soft photo backdrop of a woman in warm beige tones">
  <h2 class="section-title script" style="top:92px">Services</h2>

  <div class="svc-ring" style="left:167px;top:173px"></div>
  <div class="svc-photo" style="left:188px;top:194px;background:linear-gradient(135deg,#c8cad0,#e3c5b2 60%,#f2efec)" role="img" aria-label="Anti wrinkle injection treatment photo"></div>
  <div class="svc" style="left:163px;top:460px">Anti wrinkle injections<br>and fillers</div>

  <div class="svc-ring" style="left:464px;top:173px"></div>
  <div class="svc-photo" style="left:485px;top:194px;background:linear-gradient(160deg,#f6f1ee,#d99b84 60%,#e7b9a5)" role="img" aria-label="Neck with lifting guide arrows"></div>
  <div class="svc" style="left:460px;top:460px">Necklifts</div>

  <div class="svc-ring" style="left:759px;top:173px"></div>
  <div class="svc-photo" style="left:780px;top:194px;background:linear-gradient(135deg,#e8e3e0,#d9b394 55%,#f0d8c4)" role="img" aria-label="Brow treatment close-up"></div>
  <div class="svc" style="left:755px;top:460px">Brow lift</div>

  <div class="svc-ring" style="left:167px;top:540px"></div>
  <div class="svc-photo" style="left:188px;top:561px;background:linear-gradient(135deg,#d6d6d8,#e5c8b4 60%,#f4f2f0)" role="img" aria-label="Facial scar revision treatment photo"></div>
  <div class="svc" style="left:163px;top:827px">Facial scar revision</div>

  <div class="svc-ring" style="left:464px;top:540px"></div>
  <div class="svc-photo" style="left:485px;top:561px;background:linear-gradient(135deg,#9fb0bb,#e3cabb 55%,#f2f0ef)" role="img" aria-label="Face lift treatment photo"></div>
  <div class="svc" style="left:460px;top:827px">Rhytidectomy or Face lift</div>

  <div class="svc-ring" style="left:759px;top:540px"></div>
  <div class="svc-photo" style="left:780px;top:561px;background:linear-gradient(135deg,#eeeeee,#dcb6a4 50%,#8a6fa8)" role="img" aria-label="Chin implant treatment photo"></div>
  <div class="svc" style="left:755px;top:827px">Chin implants</div>

  <div class="btn" style="left:525px;top:910px;width:150px;height:48px">View All</div>
</section>

<!-- WHY CHOOSE US -->
<section class="why" role="img" aria-label="Dimmed photo of a face during a cosmetic consultation">
  <h2 class="section-title script" style="top:88px;color:#fff">Why Choose Us</h2>
  <div class="stat" style="left:134px;top:181px"><div class="num">4000+</div><div class="cap">Cosmetic<br>Procedures</div></div>
  <div class="stat" style="left:378px;top:181px"><div class="num">55<small>Min</small></div><div class="cap">Consultations<br>(Multiple Offered)</div></div>
  <div class="stat" style="left:622px;top:181px"><div class="num">10+</div><div class="cap">Years Of<br>Experience</div></div>
  <div class="stat" style="left:866px;top:181px"><div class="num">5<small>yr</small></div><div class="cap">Specialised Aftercare<br>With Lifetime Care</div></div>
</section>

<!-- TESTIMONIALS -->
<section>
  <h2 class="section-title script" style="top:3025px">Testimonials</h2>
  <svg class="abs" style="left:36px;top:3250px" width="20" height="26" viewBox="0 0 20 26"><path d="M14 4L6 13l8 9" stroke="#555" stroke-width="2" fill="none"/></svg>
  <svg class="abs" style="left:1144px;top:3250px" width="20" height="26" viewBox="0 0 20 26"><path d="M6 4l8 9-8 9" stroke="#555" stroke-width="2" fill="none"/></svg>

  <article class="card" style="left:87px">
    <div class="quote"><svg width="24" height="20" viewBox="0 0 24 20"><path d="M0 20V10L5 0h4L6 9h4v11zM14 20V10l5-10h4l-3 9h4v11z" fill="#fff"/></svg></div>
    <h3>Lena Marsh</h3>
    <p>Lorem ipsum dolor sit amet, tetur adipiscing elit, sed do eiusmod empor incididunt ut labore etim ad minim</p>
    <a>Read More</a>
  </article>
  <article class="card" style="left:437px">
    <div class="quote"><svg width="24" height="20" viewBox="0 0 24 20"><path d="M0 20V10L5 0h4L6 9h4v11zM14 20V10l5-10h4l-3 9h4v11z" fill="#fff"/></svg></div>
    <h3>Tessa Rowan</h3>
    <p>Lorem ipsum dolor sit amet, tetur adipiscing elit, sed do eiusmod empor incididunt ut labore etim ad minim</p>
    <a>Read More</a>
  </article>
  <article class="card" style="left:787px">
    <div class="quote"><svg width="24" height="20" viewBox="0 0 24 20"><path d="M0 20V10L5 0h4L6 9h4v11zM14 20V10l5-10h4l-3 9h4v11z" fill="#fff"/></svg></div>
    <h3>Darian Holt</h3>
    <p>Lorem ipsum dolor sit amet, tetur adipiscing elit, sed do eiusmod empor incididunt ut labore etim ad minim</p>
    <a>Read More</a>
  </article>
</section>

<!-- GALLERY -->
<section class="gallery">
  <h2 class="section-title script" style="top:92px">Gallery</h2>
  <div class="gphoto" style="left:89px;background:linear-gradient(135deg,#f1ebe8,#d9ad98 55%,#efe6e1)" role="img" aria-label="Gallery photo: woman with hands framing her face"></div>
  <div class="gphoto" style="left:297px;background:linear-gradient(135deg,#c9a48c,#e6c4ae 55%,#f0e8e3)" role="img" aria-label="Gallery photo: facial measurement before treatment"></div>
  <div class="gphoto" style="left:504px;background:linear-gradient(135deg,#d7e0ea,#ecd3c2 55%,#f4f4f6)" role="img" aria-label="Gallery photo: skin consultation"></div>
  <div class="gphoto" style="left:711px;background:linear-gradient(135deg,#f3f0ee,#d9ab90 50%,#f3f0ee)" role="img" aria-label="Gallery photo: body contour markings"></div>
  <div class="gphoto" style="left:919px;background:linear-gradient(135deg,#eeeeee,#e4c5b3 55%,#f5f3f2)" role="img" aria-label="Gallery photo: woman with smooth skin"></div>
  <div class="dots"><i></i><i></i><i></i></div>
</section>

<!-- NEWSLETTER -->
<section class="newsletter">
  <h2 class="abs script nl-title">Subscribe Our Newsletter</h2>
  <div class="nl-field"><span>Enter Your Email Address</span>
    <svg width="20" height="18" viewBox="0 0 20 18"><path d="M0 8L20 0 16 18 10 12 8 17 7 11zM7 11L18 2" fill="#555" stroke="#fff" stroke-width=".8"/></svg>
  </div>
</section>

<!-- LOCATIONS -->
<section>
  <h2 class="section-title script" style="top:4262px">Our Clinic Locations</h2>
  <div class="map" style="left:91px" role="img" aria-label="Street map of the Echuca clinic"></div>
  <div class="map" style="left:352px" role="img" aria-label="Street map of the Bendigo clinic"></div>
  <div class="map" style="left:612px" role="img" aria-label="Street map of the Epping clinic"></div>
  <div class="map" style="left:873px" role="img" aria-label="Street map of the Melbourne clinic"></div>
  <svg class="abs" style="left:199px;top:4453px" width="20" height="26" viewBox="0 0 20 26"><path d="M10 26S0 14 0 10a10 10 0 0120 0c0 4-10 16-10 16z" fill="#d93b30"/><circle cx="10" cy="10" r="4" fill="#8a1d16"/></svg>
  <svg class="abs" style="left:460px;top:4453px" width="20" height="26" viewBox="0 0 20 26"><path d="M10 26S0 14 0 10a10 10 0 0120 0c0 4-10 16-10 16z" fill="#d93b30"/><circle cx="10" cy="10" r="4" fill="#8a1d16"/></svg>
  <svg class="abs" style="left:720px;top:4453px" width="20" height="26" viewBox="0 0 20 26"><path d="M10 26S0 14 0 10a10 10 0 0120 0c0 4-10 16-10 16z" fill="#d93b30"/><circle cx="10" cy="10" r="4" fill="#8a1d16"/></svg>
  <svg class="abs" style="left:981px;top:4453px" width="20" height="26" viewBox="0 0 20 26"><path d="M10 26S0 14 0 10a10 10 0 0120 0c0 4-10 16-10 16z" fill="#d93b30"/><circle cx="10" cy="10" r="4" fill="#8a1d16"/></svg>
  <div class="loc" style="left:79px">48 Tolland Street Echuca<br>VIC 3550</div>
  <div class="loc" style="left:340px">312 Mirren Street Bendigo<br>Vic 3550</div>
  <div class="loc" style="left:600px">Level 3, 415 Hadley Street,<br>Epping Vic 3076</div>
  <div class="loc" style="left:861px">Level 6, 187 Brenton Street<br>Melbourne Vic 3000</div>
</section>

<!-- FOOTER -->
<footer class="footer">
  <svg class="abs" style="left:0;top:0" width="1200" height="500" viewBox="0 0 1200 500">
    <path d="M0 85 C200 60 500 50 690 30 L695 22 L700 30 C900 45 1080 70 1200 85 L1200 500 L0 500Z" fill="#1f1f1f"/>
    <path d="M0 75 C200 50 500 40 690 20 L695 12 L700 20 C900 35 1080 60 1200 75" stroke="#c9bd9f" stroke-width="4" fill="none"/>
  </svg>
  <div class="fcol" style="left:104px"><h4>COMPANY</h4><ul><li>Home</li><li>About</li><li>Procedures</li><li>Gallery</li><li>Contact</li></ul></div>
  <div class="fcol" style="left:354px"><h4>CONTACT US</h4><ul><li style="line-height:26px">info@mkfacialplastics.example</li><li style="line-height:26px">03 5550 1187</li></ul></div>
  <div class="fcol" style="left:688px"><h4>LEGAL</h4><ul><li style="line-height:27px">Privacy Policy</li><li style="line-height:27px">Faq</li><li style="line-height:27px">Sitemap</li></ul></div>
  <div class="fcol" style="left:928px"><h4>FOLLOW US</h4><div class="socials" aria-label="Social media links"><i></i><i></i><i></i><i></i><i></i></div></div>
  <p class="copy">© 2020 The Company Name. All rights Reserved.Privacy Policy | Terms Of Use</p>
</footer>

</body>
</html>
```